Webbanner-Design für Kampfsportschule
Super Arbeit, eine ganz tolle Zusammenarbeit! Auf alle Wünsche wurde sofort eingegangen. Die Designerin hat viel mehr gemacht, als ich erwartet habe. Sehr netter Kontakt und ein reibungsloser Ablauf. Habe mich mit meinem Projekt sehr gut aufgehoben und betreut gefühlt.
Zielgruppe
Hallo :),
nachdem mir hier vor ein paar Tagen erfolgreich so ein tolles neues Firmen Logo erstellt wurde, möchte ich gleich mit einem neuen Projekt starten.
Zuerst einmal zu uns:
Wir sind eine Kampfsportschule mit dem Schwerpunkt Krav Maga (Krav Maga ist ein taktisches israelische Selbstverteidigungs-und Nahkampfsystem mit dem Ziel mit allen Arten von Gewalt umzugehen, sie zu vermeiden, zu beseitigen oder sich gegen sie zu verteidigen) und Kickboxen.
Wir trainieren sowohl Kinder ab 4 Jahren als auch Erwachsene bis 65 Jahren in Sachen Selbstverteidigung und Kickboxen. Hauptaugenmerk liegt aber auf das Selbstverteidigungssystem Krav Maga, eine gehobene Zielgruppe für diese Kampagne zwischen 18 und 50 Jahre. Wir trainieren viele zwischen 35 - 50 Jahre, die etwas für ihre Sicherheit tun möchten.
Ich benötige jetzt einen Werbebanner, möglichst in verschiedenen Größen, in erster Linie für eine Kampagne auf Facebook. Der Banner wird dort bei einem örtlichen Medien- und Nachrichtenunternehmen regional bei den aktuellen News geschaltet, besonders Themenbezogen, wenn etwas regional passiert. Beispiel: Erneuter Messerangriff in Hamburg... Diese Nachrichtenseite schreibt über alles, was gerade aktuell in der Region passiert ist, mit polizeilichen Meldungen, Feuerwehr, Rettungsdienst usw. Und genau an dieser Stelle wird dann jeweils unser Banner platziert... Dieser Banner soll unser Selbstverteidigung System präsentieren in einem neuen edlen Design. Das neue Logo, welches mir hier entworfen wurde spiegelt genau den Stil wieder, den ich möchte und es muss unbedingt hervorstechen, gerne auch so als 3 D Version wie ein Vorschlag der Designerin war, das gefällt mir sehr gut... Ein edler Stil... sofern das möglich ist und Sinn macht...
Aufgabenstellung
Info: Ich habe mich soeben für ein Design entschieden, da es genau das ist was ich gesucht habe und warte nur noch auf andere Formate und ein paar kleine Änderungen daher kann ich es jetzt noch nicht sofort vorzeitig beenden. Für euch zur Info, damit ihr nicht noch eure Zeit für Vorschläge investiert...
-Firmen-Logo, gerne in dem edlen 3D Design, sofern möglich und sinnvoll - Ihr seid die Fachleute :)
TVU Logo
- Foto, damit man sofort darauf aufmerksam gemacht wird worum es geht?
- Homepage denke ich www.halt-stand-budo.com
-Da es regional ist vielleicht den Ort Dollern
-Krav Maga / Selbstverteidigung
Sei kein Opfer
Bereite dich vor / prepare yourself
Schütze dich selbst
- Vielleicht Hamburg als Hintergrund, da Dollern nah an Hamburg liegt und wir damit im Unterbewusstsein Großstadt / mehr Übergriffe hervorrufen?
Die Leute sollen sofort erkennen, ja, dass kann mir auch passieren und dort kann ich etwas zum Selbstschutz tun...
Letztendlich bin ich total offen für Vorschläge
Ich habe ein paar Fotos mit angehängt, das eine wo ich mit dem Mann stehe ist der Gründer der Tesh Vanar Union Oren Batzuri, mein Ausbilder und auf der TVU Werbung immer mit drauf... Trainieren vom Ursprung des Krav Maga

```html
<!DOCTYPE html>
<html lang="de">
<head>
<meta charset="utf-8">
<title>Halt Stand – Bereite dich vor</title>
<link href="https://fonts.googleapis.com/css2?family=Oswald:wght@400;500;600&display=swap" rel="stylesheet">
<style>
  :root {
    --backdrop: #8c8d8f;
    --backdrop-light: #a3a4a6;
    --panel-dark: #1b1b1c;
    --panel-darker: #141415;
    --signal-red: #e8452c;
    --white: #ffffff;
    --photo-shadow: #3a3436;
    --photo-skin: #c49a84;
    --photo-light: #d9d6d4;
    --photo-grey: #8e8f94;
    --badge: #232325;
  }
  * { box-sizing: border-box; margin: 0; padding: 0; }
  html, body {
    width: 1200px;
    height: 420px;
    overflow: hidden;
  }
  body {
    background: radial-gradient(ellipse at 50% 50%, var(--backdrop-light), var(--backdrop));
    font-family: "Oswald", "Arial Narrow", sans-serif;
    position: relative;
  }
  .banner {
    position: absolute;
    left: 95px;
    top: 142px;
    width: 1010px;
    height: 134px;
    background: var(--panel-dark);
    overflow: hidden;
  }
  .brand {
    position: absolute;
    left: 0; top: 0;
    width: 210px; height: 100%;
    background: var(--panel-darker);
    display: flex;
    flex-direction: column;
    align-items: center;
    justify-content: center;
    gap: 10px;
  }
  .brand-mark {
    width: 36px; height: 36px;
    background: var(--signal-red);
  }
  .brand-name {
    color: var(--white);
    font-weight: 500;
    font-size: 26px;
    letter-spacing: 1px;
    line-height: 1;
  }
  .location {
    position: absolute;
    left: 210px; top: 0;
    width: 40px; height: 100%;
    border-left: 2px solid var(--white);
    background: var(--panel-darker);
    display: flex;
    align-items: center;
    justify-content: center;
  }
  .location span {
    transform: rotate(-90deg);
    color: var(--white);
    font-weight: 500;
    font-size: 22px;
    letter-spacing: 2px;
    white-space: nowrap;
  }
  .photo {
    position: absolute;
    left: 250px; top: 0;
    width: 508px; height: 100%;
    background:
      radial-gradient(ellipse 120px 70px at 52% 90%, rgba(196,154,132,0.9), rgba(196,154,132,0) 100%),
      radial-gradient(ellipse 110px 80px at 78% 55%, rgba(217,214,212,0.85), rgba(217,214,212,0) 100%),
      linear-gradient(90deg, var(--panel-dark) 0%, var(--photo-shadow) 32%, var(--photo-skin) 50%, var(--photo-grey) 68%, var(--photo-light) 82%, var(--photo-grey) 100%);
  }
  .crosshair {
    position: absolute;
    left: 492px; top: -36px;
    width: 140px; height: 140px;
  }
  .tagline {
    position: absolute;
    left: 262px; top: 2px;
    width: 214px; height: 32px;
    background: var(--signal-red);
    color: var(--white);
    font-weight: 500;
    font-size: 20px;
    line-height: 32px;
    text-align: center;
    letter-spacing: 0.5px;
  }
  .partner-badge {
    position: absolute;
    left: 284px; top: 48px;
    width: 142px; height: 78px;
    background: var(--badge);
  }
  .contact {
    position: absolute;
    left: 758px; top: 0;
    width: 252px; height: 100%;
    background: var(--panel-darker);
  }
  .phone {
    position: absolute;
    left: 10px; top: 12px;
    display: flex;
    align-items: center;
    gap: 10px;
  }
  .phone svg { width: 26px; height: 26px; }
  .phone-number {
    color: var(--signal-red);
    font-weight: 400;
    font-size: 30px;
    line-height: 1;
    letter-spacing: 0.5px;
  }
  .call-to-action {
    position: absolute;
    left: 8px; top: 65px;
    width: 232px; height: 47px;
    background: var(--signal-red);
    color: var(--white);
    font-weight: 500;
    font-size: 23px;
    line-height: 47px;
    text-align: center;
    letter-spacing: 0.5px;
  }
</style>
</head>
<body>
  <section class="banner">
    <div class="brand">
      <div class="brand-mark"></div>
      <div class="brand-name">HALT STAND</div>
    </div>

    <div class="location"><span>DOLLERN</span></div>

    <div class="photo" role="img" aria-label="Foto: Ausbilder und Gründer der Tesh Vanar Union bei einer Selbstverteidigungsübung vor Stadtkulisse"></div>

    <svg class="crosshair" viewBox="0 0 140 140" aria-hidden="true">
      <circle cx="70" cy="70" r="40" fill="none" stroke="var(--white)" stroke-width="6"/>
      <line x1="70" y1="0" x2="70" y2="44" stroke="var(--white)" stroke-width="5"/>
      <line x1="70" y1="96" x2="70" y2="140" stroke="var(--white)" stroke-width="5"/>
      <line x1="0" y1="70" x2="44" y2="70" stroke="var(--white)" stroke-width="5"/>
      <line x1="96" y1="70" x2="140" y2="70" stroke="var(--white)" stroke-width="5"/>
    </svg>

    <div class="tagline">BEREITE DICH VOR</div>

    <div class="partner-badge" role="img" aria-label="Partnerzeichen Tesh Vanar Union"></div>

    <div class="contact">
      <div class="phone">
        <svg viewBox="0 0 24 24" aria-hidden="true">
          <path fill="var(--white)" d="M6.6 10.8a15.1 15.1 0 0 0 6.6 6.6l2.2-2.2c.3-.3.7-.4 1-.2 1.1.4 2.3.6 3.6.6.6 0 1 .4 1 1V20c0 .6-.4 1-1 1A17 17 0 0 1 3 4c0-.6.4-1 1-1h3.5c.6 0 1 .4 1 1 0 1.3.2 2.5.6 3.6.1.3 0 .7-.2 1z"/>
        </svg>
        <span class="phone-number">0152-31896042</span>
      </div>
      <div class="call-to-action">WERDE KEIN OPFER</div>
    </div>
  </section>
</body>
</html>
```